Veterinary hospital brochure design

we need brochure design for our veterinary hospital, something interesting, catchy and unique. Once we get going we need to add few unique services we offer and should be highlighted.Nice colors, and should be very professional looking. Brochure to be tri fold, nice colors highlight our services.
Like shades of blues or green.This is full service veterinary hospital. We do focus and specialize in Canine reproduction.

pet owners

Hospital

Serif
Script

• catchy words
• unique design
• have our unique services included
• good pictures and catchy words etc etc

```html
<!DOCTYPE html>
<html lang="en">
<head>
<meta charset="utf-8">
<title>Harbor Point Hospital for Animals – Tri-fold Brochure</title>
<link rel="stylesheet" href="https://fonts.googleapis.com/css2?family=Open+Sans:wght@400;600;700&display=swap">
<style>
  :root {
    --teal: #1f9590;
    --teal-deep: #17807f;
    --blue: #2f7fae;
    --ink-white: #ffffff;
    --accent-text: #2a93a3;
    --paper: #ffffff;
    --stage: #efefef;
    --body-dark: #333b40;
    --photo-warm-a: #c9a58c;
    --photo-warm-b: #e9e4dc;
    --photo-cat-a: #ece8e3;
    --photo-cat-b: #b9a79a;
  }
  * { box-sizing: border-box; margin: 0; padding: 0; }
  html, body { width: 1200px; height: 1200px; overflow: hidden; }
  body {
    background: var(--stage);
    font-family: "Open Sans", Arial, sans-serif;
    position: relative;
  }
  .spread {
    position: absolute;
    left: 240px;
    width: 720px;
    height: 552px;
    background: var(--paper);
    box-shadow: 0 14px 24px rgba(0,0,0,.18);
    overflow: hidden;
  }
  .spread--outside { top: 30px; }
  .spread--inside { top: 618px; }

  /* Outside */
  .about {
    position: absolute; left: 0; top: 0; width: 232px; height: 552px;
    background: linear-gradient(160deg, var(--teal) 0%, var(--blue) 100%);
    color: var(--ink-white);
    padding: 68px 26px 0 34px;
  }
  .about__title { font-size: 17px; font-weight: 400; letter-spacing: .3px; margin-left: 28px; margin-bottom: 40px; }
  .about__title b { font-weight: 700; }
  .about__text { font-size: 8.4px; line-height: 11px; }

  .cover-photo {
    position: absolute; left: 232px; top: 0; width: 488px; height: 330px;
    background: linear-gradient(120deg, var(--photo-cat-a) 0%, #ddd6cf 50%, var(--photo-cat-b) 100%);
  }
  .cover-band {
    position: absolute; left: 232px; top: 330px; width: 488px; height: 150px;
    background: linear-gradient(90deg, var(--teal) 0%, var(--blue) 100%);
    color: var(--ink-white);
  }
  .contact { position: absolute; left: 36px; top: 40px; font-size: 8.4px; line-height: 10.5px; }
  .contact__row { display: flex; align-items: flex-start; gap: 8px; margin-bottom: 11px; }
  .contact__row svg { flex: none; width: 12px; height: 12px; }
  .cover-title { position: absolute; right: 14px; top: 36px; text-align: left; }
  .cover-title h1 { font-size: 39px; font-weight: 700; line-height: 1; letter-spacing: .5px; }
  .cover-title p { font-size: 15px; font-weight: 600; margin-top: 9px; letter-spacing: .2px; }
  .cover-foot {
    position: absolute; left: 232px; top: 480px; width: 488px; height: 64px;
    background: var(--paper);
  }
  .cover-foot__url { position: absolute; left: 60px; top: 28px; font-size: 8.4px; color: var(--body-dark); }
  .brand {
    position: absolute; right: 34px; top: 17px;
    display: flex; align-items: center; gap: 7px;
    font-size: 13px; font-weight: 600; color: var(--body-dark); letter-spacing: .2px;
  }
  .brand__dot { width: 12px; height: 12px; border-radius: 50%; background: var(--body-dark); }
  .edge-strip {
    position: absolute; left: 232px; bottom: 0; width: 488px; height: 8px;
    background: linear-gradient(90deg, var(--teal), var(--blue));
  }

  /* Inside */
  .spread--inside { background: #f6f6f4; }
  .hero-photo {
    position: absolute; left: 0; top: 0; width: 484px; height: 316px;
    background: linear-gradient(110deg, #5a3f33 0%, var(--photo-warm-a) 38%, var(--photo-warm-b) 70%, #f1efe9 100%);
  }
  .quotes {
    position: absolute; left: 486px; top: 12px; width: 220px; height: 282px;
    background: linear-gradient(180deg, var(--teal) 0%, var(--blue) 100%);
    color: var(--ink-white);
    padding: 14px 14px 0 14px;
  }
  .quote { margin-bottom: 14px; }
  .quote__mark { width: 40px; height: 30px; display: block; }
  .quote__text { font-size: 8.2px; line-height: 11px; margin: 2px 0 6px 20px; }
  .quote__name { font-size: 8.2px; font-weight: 600; text-align: right; }

  .services {
    position: absolute; left: 0; top: 328px; width: 474px; height: 211px;
    background: linear-gradient(90deg, var(--blue) 0%, var(--teal) 100%);
    color: var(--ink-white);
    padding: 22px 0 0 32px;
  }
  .services__title { font-size: 17px; font-weight: 400; letter-spacing: .4px; padding-bottom: 8px; width: 388px; border-bottom: 1px solid rgba(255,255,255,.3); }
  .services__title b { font-weight: 600; }
  .services__lists { display: flex; gap: 0; margin-top: 14px; }
  .services__list { list-style: none; width: 240px; }
  .services__list li { display: flex; align-items: center; gap: 8px; font-size: 9.5px; height: 22px; }
  .paw { width: 10px; height: 10px; flex: none; }

  .promise {
    position: absolute; left: 486px; top: 328px; width: 234px; height: 211px;
    background: var(--paper);
  }
  .promise__text {
    position: absolute; left: 50px; top: 20px;
    color: var(--accent-text); font-size: 25px; font-weight: 400; line-height: 23px; letter-spacing: .3px;
  }
  .promise__text .big { font-size: 28px; }
  .promise__pets {
    position: absolute; left: 18px; top: 142px; width: 212px; height: 58px;
    background: linear-gradient(90deg, #8d8f93 0%, #8a6a4e 45%, #c7a17c 75%, #8bb46a 100%);
    border-radius: 30px 30px 6px 6px;
    opacity: .85;
  }
</style>
</head>
<body>

<section class="spread spread--outside" aria-label="Brochure outside">
  <div class="about">
    <h2 class="about__title">ABOUT <b>US</b></h2>
    <p class="about__text">Lorem ipsum dolor sit amet, consectetur adipisicing elit, sed do eiusmod tempor incididunt ut labore et dolore magna aliqua. Ut enim ad minim veniam, quis nostrud exercitation ullamco laboris nisi ut aliquip ex ea commodo consequat. Duis aute irure dolor in reprehenderit in voluptate velit esse cillum dolore eu fugiat nulla pariatur. Excepteur sint occaecat cupidatat non proident, sunt in culpa qui officia deserunt mollit anim id est laborum. Sed ut perspiciatis unde omnis iste natus error sit voluptatem accusantium doloremque laudantium, totam rem aperiam, eaque ipsa quae ab illo inventore veritatis et quasi architecto beatae vitae dicta sunt explicabo. Nemo enim ipsam voluptatem quia voluptas sit aspernatur aut odit aut fugit, sed quia consequuntur magni dolores eos qui ratione voluptatem sequi nesciunt. Neque porro quisquam est, qui dolorem ipsum quia dolor sit amet, consectetur, adipisci velit, sed quia non numquam eius modi tempora incidunt ut labore et dolore magnam aliquam quaerat voluptatem.</p>
  </div>

  <div class="cover-photo" role="img" aria-label="Photo of a fluffy blue-eyed cat held in a person's arms"></div>

  <div class="cover-band">
    <div class="contact">
      <div class="contact__row">
        <svg viewBox="0 0 12 12" aria-hidden="true"><path d="M6 0.5a4 4 0 0 1 4 4c0 3-4 7-4 7s-4-4-4-7a4 4 0 0 1 4-4z" fill="#fff"/><circle cx="6" cy="4.5" r="1.5" fill="#2a8a9a"/></svg>
        <span>12000 Yourcompanyadress,<br>yourcompanyadress</span>
      </div>
      <div class="contact__row">
        <svg viewBox="0 0 12 12" aria-hidden="true"><circle cx="6" cy="6" r="5.5" fill="#fff"/><path d="M4 3.2l1 1.6-.6.7c.4.9 1.1 1.6 2 2l.7-.6 1.6 1-.5 1.1C6 8.8 3.2 6 3 4.2z" fill="#2a8a9a"/></svg>
        <span>1200.000.000</span>
      </div>
      <div class="contact__row">
        <svg viewBox="0 0 12 12" aria-hidden="true"><circle cx="6" cy="6" r="5.5" fill="#fff"/><rect x="3" y="4" width="6" height="4" fill="none" stroke="#2a8a9a" stroke-width=".9"/><path d="M3 4l3 2.2L9 4" fill="none" stroke="#2a8a9a" stroke-width=".9"/></svg>
        <span>contact@yourcompany.com</span>
      </div>
    </div>
    <div class="cover-title">
      <h1>GOT PETS?</h1>
      <p>WE LOVE &amp; CARE FOR THEM</p>
    </div>
  </div>

  <div class="cover-foot">
    <span class="cover-foot__url">WWW.HARBORPOINTVET.COM</span>
    <div class="brand"><span class="brand__dot"></span>Harbor Point Hospital for Animals</div>
  </div>
  <div class="edge-strip"></div>
</section>

<section class="spread spread--inside" aria-label="Brochure inside">
  <div class="hero-photo" role="img" aria-label="Photo of a smiling woman hugging a pale golden retriever"></div>

  <div class="quotes">
    <div class="quote">
      <svg class="quote__mark" viewBox="0 0 40 30" aria-hidden="true"><path d="M2 28V16C2 8 6 3 14 2v5c-4 1-5 4-5 8h5v13zM22 28V16c0-8 4-13 12-14v5c-4 1-5 4-5 8h5v13z" fill="#fff" opacity=".9"/></svg>
      <p class="quote__text">Lorem ipsum dolor sit amet, consectetur adipisicing elit, sed do eiusmod tempor incididunt ut labore et dolore magna aliqua. Ut enim ad minim veniam, quis nostrud exercitation ullamco laboris nisi ut aliquip</p>
      <p class="quote__name">Jonh Doe</p>
    </div>
    <div class="quote">
      <svg class="quote__mark" viewBox="0 0 40 30" aria-hidden="true"><path d="M2 28V16C2 8 6 3 14 2v5c-4 1-5 4-5 8h5v13zM22 28V16c0-8 4-13 12-14v5c-4 1-5 4-5 8h5v13z" fill="#fff" opacity=".9"/></svg>
      <p class="quote__text">Lorem ipsum dolor sit amet, consectetur adipisicing elit, sed do eiusmod tempor incididunt ut labore et dolore magna aliqua. Ut enim ad minim veniam, quis nostrud exercitation ullamco laboris nisi ut aliquip</p>
      <p class="quote__name">Jane Doe</p>
    </div>
  </div>

  <div class="services">
    <h2 class="services__title">OUR <b>SERVICES</b></h2>
    <div class="services__lists">
      <ul class="services__list">
        <li><svg class="paw" viewBox="0 0 10 10"><g fill="#fff"><ellipse cx="5" cy="7" rx="2.4" ry="2"/><circle cx="2" cy="4" r="1"/><circle cx="4" cy="2.4" r="1"/><circle cx="6.2" cy="2.4" r="1"/><circle cx="8.2" cy="4" r="1"/></g></svg>Breeding soudness exams</li>
        <li><svg class="paw" viewBox="0 0 10 10"><g fill="#fff"><ellipse cx="5" cy="7" rx="2.4" ry="2"/><circle cx="2" cy="4" r="1"/><circle cx="4" cy="2.4" r="1"/><circle cx="6.2" cy="2.4" r="1"/><circle cx="8.2" cy="4" r="1"/></g></svg>Semen collection</li>
        <li><svg class="paw" viewBox="0 0 10 10"><g fill="#fff"><ellipse cx="5" cy="7" rx="2.4" ry="2"/><circle cx="2" cy="4" r="1"/><circle cx="4" cy="2.4" r="1"/><circle cx="6.2" cy="2.4" r="1"/><circle cx="8.2" cy="4" r="1"/></g></svg>Computer assisted semen analysis</li>
        <li><svg class="paw" viewBox="0 0 10 10"><g fill="#fff"><ellipse cx="5" cy="7" rx="2.4" ry="2"/><circle cx="2" cy="4" r="1"/><circle cx="4" cy="2.4" r="1"/><circle cx="6.2" cy="2.4" r="1"/><circle cx="8.2" cy="4" r="1"/></g></svg>Caesarian sections</li>
        <li><svg class="paw" viewBox="0 0 10 10"><g fill="#fff"><ellipse cx="5" cy="7" rx="2.4" ry="2"/><circle cx="2" cy="4" r="1"/><circle cx="4" cy="2.4" r="1"/><circle cx="6.2" cy="2.4" r="1"/><circle cx="8.2" cy="4" r="1"/></g></svg>Ovulation timing</li>
      </ul>
      <ul class="services__list">
        <li><svg class="paw" viewBox="0 0 10 10"><g fill="#fff"><ellipse cx="5" cy="7" rx="2.4" ry="2"/><circle cx="2" cy="4" r="1"/><circle cx="4" cy="2.4" r="1"/><circle cx="6.2" cy="2.4" r="1"/><circle cx="8.2" cy="4" r="1"/></g></svg>Infertility work-ups</li>
        <li><svg class="paw" viewBox="0 0 10 10"><g fill="#fff"><ellipse cx="5" cy="7" rx="2.4" ry="2"/><circle cx="2" cy="4" r="1"/><circle cx="4" cy="2.4" r="1"/><circle cx="6.2" cy="2.4" r="1"/><circle cx="8.2" cy="4" r="1"/></g></svg>Transcervical insemination</li>
        <li><svg class="paw" viewBox="0 0 10 10"><g fill="#fff"><ellipse cx="5" cy="7" rx="2.4" ry="2"/><circle cx="2" cy="4" r="1"/><circle cx="4" cy="2.4" r="1"/><circle cx="6.2" cy="2.4" r="1"/><circle cx="8.2" cy="4" r="1"/></g></svg>Surgical insemination</li>
        <li><svg class="paw" viewBox="0 0 10 10"><g fill="#fff"><ellipse cx="5" cy="7" rx="2.4" ry="2"/><circle cx="2" cy="4" r="1"/><circle cx="4" cy="2.4" r="1"/><circle cx="6.2" cy="2.4" r="1"/><circle cx="8.2" cy="4" r="1"/></g></svg>Pregnancy ultrasound</li>
        <li><svg class="paw" viewBox="0 0 10 10"><g fill="#fff"><ellipse cx="5" cy="7" rx="2.4" ry="2"/><circle cx="2" cy="4" r="1"/><circle cx="4" cy="2.4" r="1"/><circle cx="6.2" cy="2.4" r="1"/><circle cx="8.2" cy="4" r="1"/></g></svg>Semen freezing</li>
      </ul>
    </div>
  </div>

  <div class="promise">
    <p class="promise__text"><span class="big">WE LOVE</span><br>YOUR PETS<br>AS MUCH<br>AS YOU DO</p>
    <div class="promise__pets" role="img" aria-label="Photo of a row of small pets: a parrot, ferrets, a rabbit, a guinea pig and an iguana"></div>
  </div>
</section>

</body>
</html>
```